Harborline Stay Collective Business Card Design

Design a business card for Harborline Stay Collective. Look at the website for colors and reference. Card should have logo, name, title, office number, mobile number, email, URL and a tagline like, "Luxury Hotel & Resort Email Marketing" (This might change).

https://www.harborlinestaycollective.net

The rest I will leave up to your imagination.

Contact Information for Business Card

Logo, name, title, office number, mobile number, email, URL and a tagline like, "Luxury Hotel & Resort Email Marketing" (This might change).

```html
<!DOCTYPE html>
<html lang="en">
<head>
<meta charset="utf-8">
<title>Harborline Stay Collective – Business Card</title>
<link href="https://fonts.googleapis.com/css2?family=Lato:wght@400;700&family=Montserrat:wght@700;800&display=swap" rel="stylesheet">
<style>
  :root {
    --stage: #2b2c2e;
    --ink: #151616;
    --paper: #ffffff;
    --band: #dcdcde;
    --accent: #f26a12;
    --text: #222222;
  }
  * { box-sizing: border-box; margin: 0; padding: 0; }
  html, body { width: 1200px; height: 952px; overflow: hidden; }
  body {
    background: var(--stage);
    display: flex;
    align-items: center;
    justify-content: center;
    gap: 50px;
    font-family: "Lato", sans-serif;
  }
  .card {
    position: relative;
    width: 525px;
    height: 300px;
    border-radius: 22px;
    overflow: hidden;
  }

  /* Front */
  .card-front { background: var(--ink); }
  .card-front .band { position: absolute; inset: 0; }
  .brand-front {
    position: absolute;
    top: 92px; left: 0; right: 0;
    text-align: center;
    color: var(--paper);
    font-family: "Montserrat", sans-serif;
    font-weight: 800;
    font-size: 30px;
    letter-spacing: 1px;
    text-transform: uppercase;
    line-height: 1.15;
  }
  .tagline {
    position: absolute;
    left: 96px; top: 206px;
    background: var(--accent);
    color: var(--paper);
    font-size: 15px;
    font-weight: 700;
    letter-spacing: 1px;
    padding: 7px 20px;
    border-radius: 18px;
    border: 3px solid var(--ink);
  }

  /* Back */
  .card-back { background: var(--paper); color: var(--text); }
  .brand-back {
    position: absolute;
    top: 42px; right: 40px;
    width: 260px;
    text-align: right;
    font-family: "Montserrat", sans-serif;
    font-weight: 800;
    font-size: 22px;
    line-height: 1.15;
    text-transform: uppercase;
    color: var(--ink);
  }
  .person { position: absolute; top: 62px; left: 36px; }
  .person-name { font-size: 19px; letter-spacing: 0.5px; text-transform: uppercase; }
  .person-name .surname { color: var(--accent); font-weight: 700; }
  .person-title { font-size: 14px; margin-top: 4px; padding-left: 40px; }
  .contacts {
    position: absolute;
    top: 130px; left: 200px;
    display: flex;
    gap: 8px;
  }
  .icon-strip {
    width: 20px;
    background: var(--accent);
    border-radius: 4px;
    display: flex;
    flex-direction: column;
    justify-content: space-around;
    align-items: center;
    padding: 3px 0;
  }
  .icon-strip svg { width: 12px; height: 12px; }
  .contact-list { list-style: none; font-size: 13px; line-height: 21px; }
  .address {
    position: absolute;
    top: 212px; left: 36px;
    font-size: 13px;
    letter-spacing: 1px;
  }
  .rule {
    position: absolute;
    left: 200px; right: 0; top: 240px;
    height: 1.5px;
    background: var(--accent);
  }
</style>
</head>
<body>

  <section class="card card-front" aria-label="Card front">
    <svg class="band" viewBox="0 0 525 300" preserveAspectRatio="none" aria-hidden="true">
      <path d="M0 232 H330 Q350 232 350 252 V300 H0 Z" fill="var(--band)"/>
    </svg>
    <h1 class="brand-front">Harborline<br>Stay Collective</h1>
    <p class="tagline">Luxury Hotel &amp; Resort Email Marketing</p>
  </section>

  <section class="card card-back" aria-label="Card back">
    <p class="brand-back">Harborline Stay Collective</p>
    <div class="person">
      <p class="person-name">Daniel R. <span class="surname">Whitcombe</span></p>
      <p class="person-title">Managing Director</p>
    </div>
    <div class="contacts">
      <div class="icon-strip" aria-hidden="true">
        <svg viewBox="0 0 12 12"><path d="M3 1 L5 3.5 L4 5 Q5 7 7 8 L8.5 7 L11 9 L10 11 Q4 11 1 2 Z" fill="#fff"/></svg>
        <svg viewBox="0 0 12 12"><rect x="1" y="3" width="10" height="7" fill="#fff"/><path d="M1 3 L6 7 L11 3" stroke="var(--accent)" fill="none"/></svg>
        <svg viewBox="0 0 12 12"><path d="M6 1 L10 7 H7 V11 H5 V7 H2 Z" fill="#fff"/></svg>
      </div>
      <ul class="contact-list">
        <li>+00 987 654 32</li>
        <li>hello@harborlinestay.net</li>
        <li>www.harborlinestaycollective.net</li>
      </ul>
    </div>
    <p class="address">2710 Lakeview Avenue Portland, OR 97205</p>
    <div class="rule"></div>
  </section>

</body>
</html>
```